Business Advisory Firm Business Card

A clean, very upscale looking business card. Not crowded.

Please include logo (attached) and:

Daria K. Pellworth
Four Marlow Court
New York, NY 10038
tel: (332) 555-0143
fax: (347) 555-0172
email: dpellworth@quarrystoneconsultants.example
website: www.quarrystoneconsultants.example

Target Market(s)

Business clients. Often real estate development firms, other advisory firms or growing companies that need assistance. I would like a card that looks impressive and confident.

Industry/Entity Type

Business

Colors

Designer to choose colors to be used in the design.

Requirements
Must have
• Impressive and confident. Please include logo.
Should not have
• nothing flashy...

```html
<!DOCTYPE html>
<html lang="en">
<head>
<meta charset="UTF-8">
<title>Quarrystone Advisory Services — Business Card</title>
<link rel="stylesheet" href="https://fonts.googleapis.com/css2?family=Montserrat:wght@300;400;700&display=swap">
<style>
  :root {
    --backdrop: #ececec;
    --card: #ffffff;
    --ink: #2b2b2b;
    --ink-soft: #4a4a4a;
    --brand-green: #79b83a;
    --guide-line: #d2d2d2;
  }
  * { margin: 0; padding: 0; box-sizing: border-box; }
  html, body {
    width: 1200px;
    height: 800px;
    overflow: hidden;
    background: var(--backdrop);
    font-family: "Montserrat", Arial, sans-serif;
  }
  .card {
    position: absolute;
    left: 75px;
    top: 100px;
    width: 1050px;
    height: 600px;
    background: var(--card);
    box-shadow: 0 6px 24px rgba(0, 0, 0, 0.12);
    overflow: hidden;
  }
  .guide-lines {
    position: absolute;
    inset: 0;
  }
  .company {
    position: absolute;
    top: 62px;
    right: 120px;
    display: flex;
    align-items: flex-start;
    gap: 18px;
  }
  .company-mark {
    width: 22px;
    height: 22px;
    margin-top: 6px;
    background: var(--brand-green);
  }
  .company-name {
    font-weight: 700;
    font-size: 27px;
    line-height: 1.02;
    letter-spacing: 0.5px;
    font-variant: small-caps;
    color: var(--ink);
  }
  .person {
    position: absolute;
    top: 262px;
    left: 0;
    right: 0;
    height: 78px;
    display: flex;
    align-items: center;
  }
  .person-given {
    padding-left: 250px;
    padding-right: 16px;
    font-weight: 300;
    font-size: 58px;
    color: var(--ink);
    white-space: nowrap;
  }
  .person-family {
    flex: 1;
    height: 100%;
    display: flex;
    align-items: center;
    padding-left: 14px;
    background: var(--brand-green);
    font-weight: 300;
    font-size: 58px;
    color: var(--ink);
  }
  .contact {
    position: absolute;
    left: 64px;
    bottom: 58px;
    font-weight: 400;
    font-size: 19px;
    line-height: 1.3;
    color: var(--ink-soft);
    list-style: none;
  }
</style>
</head>
<body>
  <article class="card">
    <svg class="guide-lines" width="1050" height="600" viewBox="0 0 1050 600" aria-hidden="true">
      <line x1="0" y1="250" x2="1050" y2="120" stroke="var(--guide-line)" stroke-width="1.5"/>
      <line x1="0" y1="330" x2="1050" y2="430" stroke="var(--guide-line)" stroke-width="1.5"/>
      <line x1="260" y1="0" x2="120" y2="600" stroke="var(--guide-line)" stroke-width="1.5"/>
      <line x1="480" y1="0" x2="1050" y2="300" stroke="var(--guide-line)" stroke-width="1.5"/>
    </svg>

    <header class="company">
      <span class="company-mark" aria-hidden="true"></span>
      <p class="company-name">Quarrystone<br>Advisory<br>Services, Inc.</p>
    </header>

    <h1 class="person">
      <span class="person-given">Daria K.</span>
      <span class="person-family">Pellworth</span>
    </h1>

    <ul class="contact">
      <li>Four Marlow Court</li>
      <li>New York, NY 10038</li>
      <li>tel: (332) 555-0143</li>
      <li>fax: (347) 555-0172</li>
      <li>email: dpellworth@quarrystoneconsultants.example</li>
      <li>website: www.quarrystoneconsultants.example</li>
    </ul>
  </article>
</body>
</html>
```